Business Cards

Business card design for my company.
I would like the card's background colour to be black. You can also see our web site to get an idea of our brand. https://www.dlqmarrowfield.com.au/
- Name
- Email

```html
<!DOCTYPE html>
<html lang="en">
<head>
<meta charset="utf-8">
<title>DLQ Marrowfield – Business Cards</title>
<link rel="stylesheet" href="https://fonts.googleapis.com/css2?family=Open+Sans:wght@400;600;700&display=swap">
<style>
  :root {
    --stage: #2b2b2b;
    --card-black: #1f1f20;
    --card-black-light: #2c2c2e;
    --brand-green: #0a8f3f;
    --edge-green: #0b9a45;
    --ink: #141414;
    --paper: #f4f4f2;
    --muted: #3a3a3a;
    --web-grey: #d9d9d9;
    --emboss: #3d3d3f;
  }
  * { box-sizing: border-box; margin: 0; padding: 0; }
  html, body {
    width: 1200px; height: 852px; overflow: hidden;
    background: var(--stage);
    font-family: "Open Sans", Arial, sans-serif;
  }
  .sheet {
    width: 1200px; height: 852px;
    display: flex; align-items: center; justify-content: center; gap: 40px;
  }
  .card {
    position: relative;
    width: 520px; height: 300px;
    border-radius: 18px;
    overflow: hidden;
    box-shadow: 0 10px 24px rgba(0,0,0,.45);
  }

  /* Back of card */
  .card--back {
    background: linear-gradient(135deg, var(--card-black-light), var(--card-black) 60%);
    border-bottom: 5px solid var(--edge-green);
  }
  .card--back .wordmark {
    position: absolute; left: 0; right: 0; top: 112px;
    text-align: center;
    font-weight: 700; font-size: 34px; letter-spacing: 2px;
    color: var(--emboss);
    text-transform: uppercase;
  }
  .card--back .website {
    position: absolute; right: 34px; bottom: 22px;
    font-size: 14px; color: var(--web-grey);
  }

  /* Front of card */
  .card--front { background: var(--paper); }
  .card--front .green-panel {
    position: absolute; inset: 0; width: 100%; height: 100%;
  }
  .card--front .wordmark {
    position: absolute; left: 20px; top: 128px; width: 220px;
    text-align: center;
    font-weight: 700; font-size: 24px; letter-spacing: 1px;
    color: var(--ink);
    text-transform: uppercase;
    line-height: 1.2;
  }
  .details {
    position: absolute; left: 300px; top: 58px; right: 16px;
  }
  .details .name {
    font-size: 22px; font-weight: 600; color: var(--brand-green); line-height: 1.1;
  }
  .details .role {
    font-size: 13px; color: var(--muted); margin-top: 2px;
  }
  .contact-list { list-style: none; margin-top: 30px; }
  .contact-list li {
    display: flex; align-items: center; gap: 10px;
    font-size: 13px; color: var(--ink); line-height: 1; margin-bottom: 8px;
    white-space: nowrap;
  }
  .contact-list svg { width: 13px; height: 13px; flex: none; fill: var(--ink); }
</style>
</head>
<body>
<main class="sheet">

  <section class="card card--back" aria-label="Card back">
    <div class="wordmark">DLQ Marrowfield</div>
    <div class="website">www.dlqmarrowfield.com.au</div>
  </section>

  <section class="card card--front" aria-label="Card front">
    <svg class="green-panel" viewBox="0 0 520 300" preserveAspectRatio="none" aria-hidden="true">
      <path d="M0 0 H232 Q310 150 258 300 H0 Z" fill="#111"/>
      <path d="M0 0 H222 Q298 150 246 300 H0 Z" fill="var(--brand-green)"/>
    </svg>
    <div class="wordmark">DLQ<br>Marrowfield</div>

    <div class="details">
      <div class="name">Owen Harlow</div>
      <div class="role">General Manager</div>
      <ul class="contact-list">
        <li>
          <svg viewBox="0 0 24 24" aria-hidden="true"><path d="M6.6 10.8a15.1 15.1 0 0 0 6.6 6.6l2.2-2.2a1 1 0 0 1 1-.25 11.4 11.4 0 0 0 3.6.57 1 1 0 0 1 1 1V20a1 1 0 0 1-1 1A17 17 0 0 1 3 4a1 1 0 0 1 1-1h3.5a1 1 0 0 1 1 1c0 1.25.2 2.45.57 3.6a1 1 0 0 1-.25 1z"/></svg>
          0400 555 172
        </li>
        <li>
          <svg viewBox="0 0 24 24" aria-hidden="true"><path d="M2 5h20v14H2z M3.5 6.5 12 13l8.5-6.5" fill="none" stroke="#141414" stroke-width="2"/></svg>
          info@dlqmarrowfield.com.au
        </li>
        <li>
          <svg viewBox="0 0 24 24" aria-hidden="true"><circle cx="12" cy="12" r="9" fill="none" stroke="#141414" stroke-width="2"/><path d="M3 12h18M12 3c3 3 3 15 0 18M12 3c-3 3-3 15 0 18" fill="none" stroke="#141414" stroke-width="1.6"/></svg>
          www.dlqmarrowfield.com.au
        </li>
        <li>
          <svg viewBox="0 0 24 24" aria-hidden="true"><path d="M12 2a7 7 0 0 0-7 7c0 5 7 13 7 13s7-8 7-13a7 7 0 0 0-7-7zm0 9.5A2.5 2.5 0 1 1 12 6.5a2.5 2.5 0 0 1 0 5z"/></svg>
          Kelvale, Tasmania, Australia
        </li>
      </ul>
    </div>
  </section>

</main>
</body>
</html>
```